Specialised investor in e-mobility and energy wants business card design

We need a business card design that fits our existing corporate design. <The look and feel must be 'sharp'/'clean', dynamic, communicate momentum, professionalism etc (as one would imagine from a firm in the financial sector). We like the idea of a reverse-side of the card that includes the logo, and the name and contact details on the other. We expect the deliverable to be whatever format might be required to be able to get cards printed directly by a service such as tandor press. Our website is www.orm.capital

```html
<!DOCTYPE html>
<html lang="en">
<head>
<meta charset="utf-8">
<title>ORM Capital – Business Card</title>
<link href="https://fonts.googleapis.com/css2?family=Roboto:wght@300;400;500;700&display=swap" rel="stylesheet">
<style>
  :root {
    --backdrop: #979797;
    --card-green: #35532a;
    --card-green-deep: #2f4c22;
    --card-white: #ffffff;
    --ink-green: #2b4a1f;
    --accent-green: #8ab84a;
    --text-grey: #777777;
    --band-green: #223f14;
    --logo-green: #1f3a14;
  }
  * { margin: 0; padding: 0; box-sizing: border-box; }
  html, body {
    width: 1200px; height: 1000px; overflow: hidden;
    background: var(--backdrop);
    font-family: "Roboto", Arial, sans-serif;
  }
  .canvas { position: relative; width: 1200px; height: 1000px; }
  .card {
    position: absolute; left: 293px; width: 615px; height: 351px; overflow: hidden;
  }
  .card--reverse {
    top: 100px;
    background: var(--card-green);
    display: flex; align-items: center; justify-content: center;
  }
  .reverse-mark {
    font-weight: 700; font-size: 240px; line-height: 1;
    letter-spacing: -4px;
    color: var(--card-green-deep);
  }
  .card--front { top: 511px; background: var(--card-white); }
  .person { position: absolute; left: 35px; top: 55px; }
  .person__name { font-weight: 700; font-size: 22px; color: var(--ink-green); line-height: 30px; }
  .person__role { font-weight: 300; font-size: 23px; color: var(--accent-green); line-height: 28px; }
  .location {
    position: absolute; left: 34px; top: 153px;
    font-size: 18px; color: var(--text-grey);
  }
  .contacts { position: absolute; left: 35px; top: 204px; list-style: none; }
  .contacts li {
    display: flex; align-items: center; height: 26.5px;
    font-size: 18px; color: var(--text-grey);
  }
  .contacts svg { width: 18px; height: 18px; margin-right: 9px; fill: var(--accent-green); }
  .contacts svg.icon-web { fill: none; stroke: var(--accent-green); stroke-width: 1.4; }
  .brand {
    position: absolute; right: 35px; top: 246px;
    display: flex; align-items: center; gap: 10px;
    font-size: 30px; font-weight: 400; color: var(--logo-green);
  }
  .brand__dot { width: 12px; height: 12px; border-radius: 50%; background: var(--logo-green); }
  .rule-accent { position: absolute; left: 0; top: 313px; width: 100%; height: 4px; background: var(--accent-green); }
  .rule-band { position: absolute; left: 0; top: 320px; width: 100%; height: 31px; background: var(--band-green); }
</style>
</head>
<body>
<main class="canvas">
  <section class="card card--reverse">
    <span class="reverse-mark">ORM</span>
  </section>

  <section class="card card--front">
    <div class="person">
      <div class="person__name">Daniel Hartwell</div>
      <div class="person__role">Partner</div>
    </div>
    <div class="location">Geneva, Switzerland</div>
    <ul class="contacts">
      <li>
        <svg viewBox="0 0 18 18"><path d="M5 0h8a1.5 1.5 0 0 1 1.5 1.5v15A1.5 1.5 0 0 1 13 18H5a1.5 1.5 0 0 1-1.5-1.5v-15A1.5 1.5 0 0 1 5 0zm0.5 2v12h7V2zm3.5 13a1 1 0 1 0 0 2a1 1 0 0 0 0-2z"/></svg>
        +41 79548 2271
      </li>
      <li>
        <svg viewBox="0 0 18 18"><path d="M1 4h16v11H1zm1.5 1.2v0.4L9 10l6.5-4.4v-0.4zm0 2.2v6.4h13V7.4L9 11.8z"/></svg>
        daniel@orm.capital
      </li>
      <li>
        <svg class="icon-web" viewBox="0 0 18 18"><circle cx="9" cy="9" r="6.5"/><ellipse cx="9" cy="9" rx="2.8" ry="6.5"/><path d="M2.5 9h13M3.5 5.8h11M3.5 12.2h11"/></svg>
        www.orm.capital
      </li>
    </ul>
    <div class="brand"><span class="brand__dot"></span>ORM Capital</div>
    <div class="rule-accent"></div>
    <div class="rule-band"></div>
  </section>
</main>
</body>
</html>
```